Drowning Victims Recovery Website Design

We are working with Bluewake Recovery Dive Team. They provide recovery services for drowning victims so they can be reunited with their loved ones.

Some sites to use for inspiration:

https://cornerstoneplovik.org
https://www.steadfastmend.org
https://www.givingwellspring.org
https://www.pulsaid.ca/en

Thank you for taking the time to consider designing a website for us. We are web developers based in Stockton, CA, USA. Most of our projects go through the same process. Understanding this process may help you win a project with us. We custom-code all of our websites in-house. We don’t have any requirements as to what tools you use for your design, but we prefer Figma files. For any design that we label as four-stars, we send it to the client for review. The client picks the final design they want us to use. Once we complete this process, we will continue to show additional clients all the four-star sites and purchase them later. Your designs will have multiple chances to sell. For better chances of success, we ask that you follow these guidelines.

IMAGES:
If you use any images or icons in the design, we ask that you have a link to the asset so we can purchase the image/icon. Most of the designs we submit do not have the customer’s images on them unless they have some great images. Be creative; show us the feeling you are trying to portray with your image choices. Use any royalty-free site you choose. We subscribe to Varnex and mainly use their images, but we can purchase images outside of Varnex.

PLEASE NOTE: we will not submit designs to clients with watermarks on the images.

FONTS:
We ask that you identify the fonts used in the design. This can be done in a message if you want. We typically use Google Fonts and Varnex Fonts.

CONTENT:
We're always open to different content and ideas. We often submit designs with stock images so the client can see our vision. We typically take pictures after the website launch to use their images with our vision. Lorem Ipsum is fine for paragraphs, but we ask that you write the headers in correct English. We want to be able to show the vision and identify the sections of the website.

INSPIRATION:
We typically add a couple of links in the brief of websites we like to help you get started in your design.

REVISIONS:
We do not often ask for revisions of the designs unless we see something in the design that may not appeal to the client. If there are slight changes that we want to make, we do that in the development process.

FEEDBACK:
We rarely give feedback on designs during the design process. We are working on many website projects and do not have the time to provide feedback. We usually respond if your request is well thought out and asks specific questions, but a note asking “feedback, please” usually goes unanswered.

```html
<!DOCTYPE html>
<html lang="en">
<head>
<meta charset="utf-8">
<title>Bluewake</title>
<link href="https://fonts.googleapis.com/css2?family=Poppins:wght@400;500;600;700;800&display=swap" rel="stylesheet">
<style>
:root{
  --red:#c8102e;
  --navy:#0a2748;
  --navy-deep:#061b35;
  --blue:#1565c0;
  --sky:#2f8fe0;
  --pale:#eaf3fb;
  --ink:#1d2433;
  --muted:#5b6475;
  --white:#ffffff;
  --gold:#f5b301;
}
*{box-sizing:border-box;margin:0;padding:0}
html,body{width:1200px;height:3264px;overflow:hidden}
body{font-family:"Poppins",sans-serif;color:var(--ink);background:var(--white);position:relative}
.abs{position:absolute}
.btn{display:inline-block;background:var(--navy);color:var(--white);font-size:12px;font-weight:600;letter-spacing:.06em;padding:11px 24px;border-radius:22px;text-transform:uppercase;line-height:1.2}
.btn.light{background:var(--blue)}
.section-title{font-size:32px;font-weight:800;color:var(--red);text-transform:uppercase;text-align:center}
.section-title.white{color:var(--white)}

/* header */
.site-header{left:0;top:0;width:1200px;height:48px;background:var(--white);display:flex;align-items:center;padding:0 32px;box-shadow:0 2px 6px rgba(0,0,0,.06);z-index:2}
.brand{display:flex;align-items:center;gap:8px;color:var(--navy);font-weight:600;font-size:18px;width:170px}
.brand .dot{width:14px;height:14px;border-radius:50%;background:var(--blue);flex:none}
.main-nav{display:flex;gap:30px;margin-left:280px;font-size:12px;font-weight:500}
.main-nav a{color:var(--ink);text-decoration:none}
.main-nav a.active{color:var(--red)}
.header-cta{margin-left:auto;display:flex;align-items:center;gap:14px}
.header-cta .btn{padding:8px 18px;font-size:10px}
.call{display:flex;align-items:center;gap:8px;font-size:10px;line-height:1.2}
.call b{display:block;font-size:12px;color:var(--navy)}
.call .ico{width:24px;height:24px;border-radius:50%;background:var(--navy);display:flex;align-items:center;justify-content:center}

/* hero */
.hero{left:0;top:48px;width:1200px;height:520px;background:linear-gradient(120deg,#0b3350 0%,#1a5872 35%,#c07a3a 62%,#2a3d4f 80%,#0d2236 100%);overflow:hidden}
.hero .shade{position:absolute;inset:0;background:linear-gradient(90deg,rgba(4,20,40,.75) 0%,rgba(4,20,40,.25) 50%,rgba(4,20,40,.1) 100%)}
.hero-copy{position:absolute;left:190px;top:110px;width:420px;color:var(--white)}
.hero-copy h1{font-size:38px;font-weight:800;line-height:1.12;text-transform:uppercase}
.hero-copy p{font-size:14px;margin-top:10px;line-height:1.45}
.hero-copy .btn{margin-top:24px;background:var(--blue)}
.hero-wave{position:absolute;left:0;bottom:0}

/* about */
.about-title{left:160px;top:680px;font-size:32px;font-weight:800;color:var(--red)}
.about-photo{left:160px;top:734px;width:452px;height:150px;background:linear-gradient(90deg,#2b6e86,#5ea6b4 45%,#3c7a8a);border-radius:2px}
.about-text{left:160px;top:900px;width:460px;font-size:12px;line-height:1.6;color:var(--muted)}
.about-btn{left:160px;top:1008px}
.give-card{left:720px;top:690px;width:328px;height:350px;background:var(--pale);padding:22px 20px}
.give-toggle{display:flex;gap:24px;font-size:12px;font-weight:600;color:var(--navy)}
.give-toggle span{display:flex;align-items:center;gap:6px}
.give-toggle i{width:12px;height:12px;border-radius:50%;border:2px solid var(--navy)}
.give-toggle i.on{background:var(--navy);box-shadow:inset 0 0 0 2px var(--pale)}
.give-card h3{font-size:18px;font-weight:700;color:var(--navy);line-height:1.25;margin-top:18px;text-transform:uppercase}
.amounts{display:grid;grid-template-columns:1fr 1fr 1fr;gap:6px;margin-top:16px}
.amounts span{background:var(--white);border:1px solid #c9d6e4;font-size:10px;padding:9px 6px;color:var(--muted);text-align:center}
.amounts span.sel{background:var(--red);border-color:var(--red);color:var(--white)}
.give-card .btn{margin-top:18px;font-size:11px;padding:9px 20px}
.give-card small{display:block;margin-top:14px;font-size:10px;line-height:1.5;color:var(--muted)}

/* stats */
.stats{left:0;top:1128px;width:1200px;height:390px;background:linear-gradient(180deg,var(--navy),#0c3563 70%,var(--navy))}
.stats-row{position:absolute;left:200px;top:140px;width:800px;display:flex;justify-content:space-between;text-align:center;color:var(--white)}
.stat{width:170px}
.stat svg{display:block;margin:0 auto 10px}
.stat b{display:block;font-size:32px;font-weight:700}
.stat span{font-size:11px;letter-spacing:.08em;text-transform:uppercase;opacity:.85}

/* blogs */
.blogs-title{left:0;top:1600px;width:1200px}
.blog-grid{left:160px;top:1660px;width:888px;display:flex;justify-content:space-between}
.blog-card{width:282px;height:318px;position:relative;color:var(--white);overflow:hidden}
.blog-card .date{position:absolute;left:12px;top:12px;width:44px;background:var(--red);font-size:10px;font-weight:600;text-align:center;padding:6px 0;line-height:1.3}
.blog-card h4{position:absolute;left:16px;right:16px;bottom:44px;font-size:16px;font-weight:700;line-height:1.3}
.blog-card p{position:absolute;left:16px;bottom:16px;font-size:11px;font-weight:600}
.blog-card .veil{position:absolute;inset:0;background:linear-gradient(180deg,rgba(0,0,0,0) 40%,rgba(3,20,40,.8))}
.p1{background:linear-gradient(180deg,#3f88a8,#1d5672)}
.p2{background:linear-gradient(180deg,#1b4a6a,#0d2a44)}
.p3{background:linear-gradient(180deg,#9cc9dc,#2a7c99)}
.blogs-btn{left:0;top:2010px;width:1200px;text-align:center}

/* events */
.events{left:0;top:2100px;width:1200px;height:480px;background:linear-gradient(180deg,#0c3a6a,var(--navy-deep))}
.events-title{left:0;top:2180px;width:1200px}
.event-grid{left:160px;top:2240px;width:888px;display:flex;justify-content:space-between}
.event-card{width:432px;height:170px;background:var(--white);display:flex;padding:12px;gap:14px}
.event-card .ph{width:196px;height:146px;flex:none}
.event-card h4{font-size:17px;font-weight:700;line-height:1.3;color:var(--navy);margin-top:6px}
.event-meta{display:flex;align-items:center;gap:8px;margin-top:12px;font-size:11px;color:var(--red);line-height:1.4}
.event-meta svg{flex:none}
.events-btn{left:0;top:2432px;width:1200px;text-align:center}

/* testimonials */
.testi-title{left:0;top:2620px;width:1200px;color:var(--navy)}
.arrow{width:16px;height:16px}
.quote-box{left:260px;top:2720px;width:130px;height:150px;background:var(--navy);display:flex;align-items:center;justify-content:center}
.testi-body{left:408px;top:2690px;width:620px}
.stars{color:var(--gold);font-size:16px;letter-spacing:3px}
.testi-body p{font-size:12px;line-height:1.7;color:var(--muted);margin-top:8px}
.reviewer{display:flex;align-items:center;gap:12px;margin-top:16px}
.avatar{width:44px;height:44px;border-radius:50%;background:linear-gradient(180deg,#c99b86,#7d5b4c);border:3px solid var(--red)}
.reviewer-name b{display:block;font-size:13px;color:var(--navy)}
.reviewer-name span{font-size:10px;color:var(--muted)}
.reviewer .btn{margin-left:24px;padding:9px 20px;font-size:11px;color:var(--white)}

/* footer */
.site-footer{left:0;top:2930px;width:1200px;height:334px;background:var(--navy-deep);color:var(--white)}
.footer-cols{position:absolute;left:140px;top:110px;width:920px;display:flex;gap:60px}
.footer-brand{width:200px;display:flex;align-items:center;gap:10px;height:30px;color:var(--white);font-weight:600;font-size:22px}
.footer-brand .dot{width:18px;height:18px;border-radius:50%;background:var(--sky);flex:none}
.fcol h5{font-size:15px;font-weight:600;color:var(--sky);margin-bottom:12px}
.fcol li{list-style:none;font-size:11px;line-height:2.1;display:flex;gap:8px;align-items:flex-start}
.fcol.contact{width:200px}
.fcol.links{width:140px}
.news input{display:block;width:220px;height:32px;border:none;background:var(--white);font:11px "Poppins",sans-serif;padding:0 10px;color:var(--muted)}
.news .btn{margin-top:10px;background:var(--blue);padding:8px 18px;font-size:10px}
.footer-bar{position:absolute;left:0;bottom:0;width:1200px;height:34px;background:#04142a;display:flex;align-items:center;padding:0 40px;font-size:10px;opacity:.95}
.socials{margin-left:auto;display:flex;gap:8px}
.socials i{width:16px;height:16px;border-radius:50%;background:var(--sky)}
</style>
</head>
<body>

<header class="site-header abs">
  <div class="brand"><span class="dot"></span><span>Bluewake</span></div>
  <nav class="main-nav">
    <a class="active">Home</a><a>About Us</a><a>Blogs</a><a>Events</a><a>Testimonials</a>
  </nav>
  <div class="header-cta">
    <span class="btn">Contact Us</span>
    <div class="call">
      <span class="ico"><svg width="12" height="12" viewBox="0 0 24 24"><path fill="#fff" d="M6.6 10.8a15 15 0 0 0 6.6 6.6l2.2-2.2c.3-.3.7-.4 1-.2 1.1.4 2.3.6 3.6.6.6 0 1 .4 1 1V20c0 .6-.4 1-1 1A17 17 0 0 1 3 4c0-.6.4-1 1-1h3.5c.6 0 1 .4 1 1 0 1.3.2 2.5.6 3.6.1.3 0 .7-.2 1z"/></svg></span>
      <span>Call Us<b>(555) 204-7719</b></span>
    </div>
  </div>
</header>

<section class="hero abs" role="img" aria-label="Scuba diver descending through dark water toward a bright sunset surface">
  <div class="shade"></div>
  <div class="hero-copy">
    <h1>Organization for Clean and Safe Water</h1>
    <p>Lorem ipsum is simply dummy text of the printing and typesetting industry.</p>
    <span class="btn">Donate Now</span>
  </div>
  <svg class="hero-wave" width="1200" height="90" viewBox="0 0 1200 90" preserveAspectRatio="none">
    <path fill="#0d4f9a" d="M0 30 C150 0 300 60 450 35 S750 0 900 30 1100 55 1200 20 V90 H0z"/>
    <path fill="#2f8fe0" d="M0 50 C200 20 350 75 550 50 S850 20 1000 48 1150 60 1200 40 V90 H0z"/>
    <path fill="#ffffff" d="M0 68 C200 45 380 90 600 66 S950 45 1200 62 V90 H0z"/>
  </svg>
</section>

<h2 class="about-title abs">ABOUT US</h2>
<div class="about-photo abs" role="img" aria-label="Diver swimming over a reef in clear shallow water"></div>
<p class="about-text abs">Lorem Ipsum is simply dummy text of the printing and typesetting industry. Lorem Ipsum has been the industry's standard dummy text ever since the 1500s, when an unknown printer took a galley of type and scrambled it to make a type specimen book. It has survived not only five centuries, but also the leap into electronic typesetting, remaining essentially unchanged.</p>
<span class="btn about-btn abs">Read More</span>

<aside class="give-card abs">
  <div class="give-toggle"><span><i class="on"></i>Give Once</span><span><i></i>Monthly</span></div>
  <h3>Choose an amount to<br>give per month</h3>
  <div class="amounts">
    <span>$10/Month</span><span>$25/Month</span><span class="sel">$50/Month</span>
    <span>$100/Month</span><span>$250/Month</span><span>Other Amount</span>
  </div>
  <span class="btn">Join Today</span>
  <small>Your $50 monthly donation can give 12 people clean water every year. 100% funds water projects.</small>
</aside>

<section class="stats abs">
  <div class="stats-row">
    <div class="stat">
      <svg width="34" height="34" viewBox="0 0 24 24" fill="none" stroke="#fff" stroke-width="1.6"><rect x="3" y="5" width="18" height="16" rx="2"/><path d="M3 10h18M8 3v4M16 3v4"/></svg>
      <b>14 YEAR</b><span>Of Experience</span>
    </div>
    <div class="stat">
      <svg width="34" height="34" viewBox="0 0 24 24" fill="none" stroke="#fff" stroke-width="1.6"><circle cx="12" cy="12" r="9"/><path d="M12 6v12M15 9c0-1.2-1.3-2-3-2s-3 .8-3 2 1.3 2 3 2 3 .8 3 2-1.3 2-3 2-3-.8-3-2"/></svg>
      <b>$21M</b><span>Funds Collected</span>
    </div>
    <div class="stat">
      <svg width="34" height="34" viewBox="0 0 24 24" fill="none" stroke="#fff" stroke-width="1.6"><circle cx="8" cy="8" r="3"/><circle cx="16" cy="8" r="3"/><path d="M2 20c0-3.3 2.7-6 6-6s6 2.7 6 6M10 20c0-3.3 2.7-6 6-6s6 2.7 6 6"/></svg>
      <b>56</b><span>Volunteers Involved</span>
    </div>
    <div class="stat">
      <svg width="34" height="34" viewBox="0 0 24 24" fill="none" stroke="#fff" stroke-width="1.6"><path d="M12 3c3 4 6 7.5 6 11a6 6 0 0 1-12 0c0-3.5 3-7 6-11z"/></svg>
      <b>586</b><span>Families Reunited</span>
    </div>
  </div>
</section>

<h2 class="section-title blogs-title abs">Our Blogs</h2>
<div class="blog-grid abs">
  <article class="blog-card p1" role="img" aria-label="Diver floating near the water surface">
    <div class="veil"></div><span class="date">Jan 15<br>2025</span>
    <h4>Lorem Ipsum is Simply Dummy Text Of The Printing And Typesetting Industry.</h4><p>Read More</p>
  </article>
  <article class="blog-card p2" role="img" aria-label="Divers exploring a deep underwater cavern">
    <div class="veil"></div><span class="date">Jan 15<br>2025</span>
    <h4>Lorem Ipsum is Simply Dummy Text Of The Printing And Typesetting Industry.</h4><p>Read More</p>
  </article>
  <article class="blog-card p3" role="img" aria-label="Diver holding a regulator underwater">
    <div class="veil"></div><span class="date">Jan 15<br>2025</span>
    <h4>Lorem Ipsum is Simply Dummy Text Of The Printing And Typesetting Industry.</h4><p>Read More</p>
  </article>
</div>
<div class="blogs-btn abs"><span class="btn">View All</span></div>

<section class="events abs">
  <svg class="abs" style="left:0;top:0" width="1200" height="40" viewBox="0 0 1200 40" preserveAspectRatio="none"><path fill="#ffffff" d="M0 0 H1200 V12 C1000 40 800 0 600 20 S200 35 0 14z"/></svg>
</section>
<h2 class="section-title white events-title abs">Upcoming Event</h2>
<div class="event-grid abs">
  <article class="event-card">
    <div class="ph" role="img" aria-label="Boat with divers preparing on the water" style="background:linear-gradient(180deg,#f0a35a,#3e7fa6)"></div>
    <div>
      <h4>Lorem Ipsum is simply dummy text of the printing industry.</h4>
      <div class="event-meta"><svg width="20" height="20" viewBox="0 0 24 24" fill="none" stroke="#c8102e" stroke-width="1.8"><rect x="3" y="5" width="18" height="16" rx="2"/><path d="M3 10h18"/></svg><span>Jan 15, 2025<br>7:00 AM - 9:00 AM</span></div>
    </div>
  </article>
  <article class="event-card">
    <div class="ph" role="img" aria-label="Diver swimming in bright blue water" style="background:linear-gradient(180deg,#4aa8e0,#0f4f8a)"></div>
    <div>
      <h4>Lorem Ipsum is simply dummy text of the printing industry.</h4>
      <div class="event-meta"><svg width="20" height="20" viewBox="0 0 24 24" fill="none" stroke="#c8102e" stroke-width="1.8"><rect x="3" y="5" width="18" height="16" rx="2"/><path d="M3 10h18"/></svg><span>Jan 15, 2025<br>7:00 AM - 9:00 AM</span></div>
    </div>
  </article>
</div>
<div class="events-btn abs"><span class="btn light">View All</span></div>

<h2 class="section-title testi-title abs" style="color:var(--navy)">Testimonials</h2>
<svg class="abs arrow" style="left:168px;top:2752px" viewBox="0 0 16 16"><path d="M10 3 5 8l5 5" fill="none" stroke="#0a2748" stroke-width="2"/></svg>
<svg class="abs arrow" style="left:1030px;top:2752px" viewBox="0 0 16 16"><path d="m6 3 5 5-5 5" fill="none" stroke="#0a2748" stroke-width="2"/></svg>
<div class="quote-box abs">
  <svg width="56" height="44" viewBox="0 0 56 44"><path fill="#fff" d="M0 24C0 10 8 2 20 0v8c-6 2-9 6-9 12h9v24H0zM32 24C32 10 40 2 52 0v8c-6 2-9 6-9 12h9v24H32z"/></svg>
</div>
<div class="testi-body abs">
  <div class="stars">★★★★★</div>
  <p>Lorem Ipsum Is Simply Dummy Text Of The Printing And Typesetting Industry. Lorem Ipsum Has Been The Industry's Standard Dummy Text Ever Since The 1500s, When An Unknown Printer Took A Galley Of Type And Scrambled It To Make A Type Specimen Book. It Has Survived Not Only Five Centuries, But Also The Leap Into Electronic Typesetting, Remaining Essentially Unchanged.</p>
  <div class="reviewer">
    <span class="avatar" role="img" aria-label="Reviewer portrait"></span>
    <div class="reviewer-name"><b>Mara L.</b><span>Volunteer</span></div>
    <span class="btn">View All</span>
  </div>
</div>

<footer class="site-footer abs">
  <svg class="abs" style="left:0;top:0" width="1200" height="70" viewBox="0 0 1200 70" preserveAspectRatio="none">
    <path fill="#ffffff" d="M0 0H1200V30C1000 60 800 10 600 35S200 55 0 28z"/>
    <path fill="#2f8fe0" d="M0 28C200 55 400 15 600 35S1000 60 1200 30V44C1000 70 800 24 600 48S200 66 0 42z"/>
  </svg>
  <div class="footer-cols">
    <div class="footer-brand"><span class="dot"></span><span>Bluewake</span></div>
    <div class="fcol contact">
      <h5>Contact Us</h5>
      <ul>
        <li><svg width="12" height="12" viewBox="0 0 24 24" style="margin-top:6px"><path fill="#2f8fe0" d="M6.6 10.8a15 15 0 0 0 6.6 6.6l2.2-2.2c.3-.3.7-.4 1-.2 1.1.4 2.3.6 3.6.6.6 0 1 .4 1 1V20c0 .6-.4 1-1 1A17 17 0 0 1 3 4c0-.6.4-1 1-1h3.5c.6 0 1 .4 1 1 0 1.3.2 2.5.6 3.6.1.3 0 .7-.2 1z"/></svg>(555) 204-7719</li>
        <li><svg width="12" height="12" viewBox="0 0 24 24" style="margin-top:6px"><rect x="2" y="5" width="20" height="14" rx="2" fill="none" stroke="#2f8fe0" stroke-width="2"/><path d="m2 6 10 7 10-7" fill="none" stroke="#2f8fe0" stroke-width="2"/></svg>info@bluewake-dive.org</li>
        <li><svg width="12" height="12" viewBox="0 0 24 24" style="margin-top:6px"><path fill="#2f8fe0" d="M12 2a7 7 0 0 0-7 7c0 5 7 13 7 13s7-8 7-13a7 7 0 0 0-7-7zm0 9.5A2.5 2.5 0 1 1 12 6.5a2.5 2.5 0 0 1 0 5z"/></svg><span>418 Harbor Lane<br>Stillwater, CA 95210</span></li>
      </ul>
    </div>
    <div class="fcol links">
      <h5>Quick Links</h5>
      <ul><li>About Us</li><li>Blogs</li><li>Events</li><li>Testimonials</li><li>Contact Us</li></ul>
    </div>
    <div class="fcol news">
      <h5>Subscribe to Our<br>Newsletter</h5>
      <input type="text" value="Enter Email" aria-label="Email address">
      <span class="btn">Subscribe</span>
    </div>
  </div>
  <div class="footer-bar">
    <span>Copyright © 2025 Bluewake. All rights reserved.</span>
    <div class="socials"><i></i><i></i><i></i></div>
  </div>
</footer>

</body>
</html>
```